Crest Path Profile Bacground Needed

I need a simple Crest Path Background graphic for my Crest Path profile. My website is www.MorvexBLD.com
I have attached a couple of photos and our logo.

The tag line is: BEAUTY | FUNCTION | ON TIME | ON BUDGET

```html
<!DOCTYPE html>
<html lang="en">
<head>
<meta charset="utf-8">
<title>Crest Path Background Banner – Morvex Kitchen &amp; Bath</title>
<link rel="stylesheet" href="https://fonts.googleapis.com/css2?family=Arimo:wght@400&family=Archivo+Narrow:wght@400;500&display=swap">
<style>
  :root {
    --sheet-bg: #ffffff;
    --ink: #111111;
    --rule: #111111;
    --tag-text: #ffffff;
    --photo-sea: #7fb6c8;
    --photo-greenery: #9cbf86;
    --photo-tile: #a9c7d3;
    --photo-cabinet: #e9ecec;
    --photo-tub: #f4f5f4;
    --photo-floor: #d4d0c8;
  }
  * { margin: 0; padding: 0; box-sizing: border-box; }
  html, body {
    width: 1200px;
    height: 631px;
    overflow: hidden;
    background: var(--sheet-bg);
  }
  .spec-sheet {
    position: relative;
    width: 1200px;
    height: 631px;
    background: var(--sheet-bg);
    border: 1px solid #e4e4e4;
  }
  .spec-header,
  .spec-font {
    position: absolute;
    top: 96px;
    font-family: "Arimo", Arial, sans-serif;
    font-size: 27px;
    line-height: 43px;
    color: var(--ink);
  }
  .spec-header { left: 78px; }
  .spec-font { left: 520px; }
  .spec-rule {
    position: absolute;
    left: 79px;
    top: 190px;
    width: 1043px;
    height: 2px;
    background: var(--rule);
  }
  .banner {
    position: absolute;
    left: 79px;
    top: 267px;
    width: 1043px;
    height: 261px;
    overflow: hidden;
  }
  .banner-photo {
    position: absolute;
    inset: 0;
    background: linear-gradient(180deg,
      var(--photo-sea) 0%,
      var(--photo-sea) 10%,
      var(--photo-greenery) 24%,
      var(--photo-greenery) 30%,
      var(--photo-tile) 44%,
      var(--photo-cabinet) 60%,
      var(--photo-tub) 78%,
      var(--photo-floor) 100%);
  }
  .brand-lockup {
    position: absolute;
    left: 688px;
    top: 66px;
    display: flex;
    align-items: flex-start;
    gap: 12px;
    color: var(--ink);
    font-family: "Archivo Narrow", "Arial Narrow", sans-serif;
    font-weight: 500;
  }
  .brand-mark {
    width: 20px;
    height: 20px;
    margin-top: 14px;
    background: var(--ink);
  }
  .brand-name {
    display: flex;
    flex-direction: column;
    line-height: 1;
  }
  .brand-name__main {
    font-size: 60px;
    letter-spacing: 3px;
  }
  .brand-name__sub {
    font-size: 19px;
    letter-spacing: 5px;
    margin-top: 4px;
  }
  .tagline {
    position: absolute;
    left: 307px;
    top: 207px;
    font-family: "Archivo Narrow", "Arial Narrow", sans-serif;
    font-weight: 400;
    font-size: 36px;
    letter-spacing: 0.6px;
    line-height: 1;
    white-space: nowrap;
    color: var(--tag-text);
    text-shadow: 0 1px 3px rgba(0, 0, 0, 0.55);
  }
</style>
</head>
<body>
  <main class="spec-sheet">
    <div class="spec-header">
      <p class="spec-title">Crest Path Background Banner</p>
      <p class="spec-size">Size: 1776 px x 444 px</p>
    </div>
    <p class="spec-font">Font: Franklin Gothic Book</p>
    <div class="spec-rule"></div>

    <section class="banner">
      <div class="banner-photo" role="img" aria-label="Bright coastal bathroom with white shaker vanities, pale blue tile, a freestanding white tub and windows looking out to palms and the ocean"></div>
      <div class="brand-lockup">
        <span class="brand-mark"></span>
        <div class="brand-name">
          <span class="brand-name__main">MORVEX</span>
          <span class="brand-name__sub">KITCHEN &amp; BATH</span>
        </div>
      </div>
      <p class="tagline">BEAUTY | FUNCTION | ON TIME | ON BUDGET</p>
    </section>
  </main>
</body>
</html>
```